Brochure Design Project

I am a Brightwall Coatings specializing in repainting existing Commercial and Industrial building only in the Auckland N.Z market. I am looking for a tri fold brochure that will be fit into an envelope 130mm x 235mm x 6mm that I can post and also hand to perspective clients when cold calling. Please visit my web site www.brightwallcoatings.co.nz for an overview. I would like the brochure to reflect the web site. Thank you

Reason: To All designers. I am extending the deadline for 7 Days as i have been unable to spend the time to view all design submitted. Thank you all for your effort so far.

Target Market(s)

Property Managers, Building Owners, Building Tenants,

Industry/Entity Type

Building

```html
<!DOCTYPE html>
<html lang="en">
<head>
<meta charset="utf-8">
<title>Brightwall Coatings – Tri-fold Brochure</title>
<link href="https://fonts.googleapis.com/css2?family=Archivo+Black&family=Open+Sans:wght@400;700;800&display=swap" rel="stylesheet">
<style>
  :root {
    --page: #ffffff;
    --frame: #9a9a9a;
    --black: #231f20;
    --yellow: #ffdd1f;
    --red: #ef4135;
    --green: #8dc63f;
    --blue: #29a9e0;
    --pink: #ec008c;
    --link-blue: #27aae1;
    --ink-light: #ffffff;
    --heading-ghost: rgba(255,255,255,0.62);
  }
  * { box-sizing: border-box; margin: 0; padding: 0; }
  html, body { width: 1200px; height: 900px; overflow: hidden; background: var(--page); }
  .canvas { position: relative; width: 1200px; height: 900px; font-family: "Open Sans", Arial, sans-serif; }

  .sheet { position: absolute; border: 1px solid var(--frame); background: var(--page); }
  .sheet--outside { left: 28px; top: 28px; width: 627px; height: 442px; }
  .sheet--inside { left: 548px; top: 460px; width: 628px; height: 415px; }
  .fold { position: absolute; top: 0; bottom: 0; width: 1px; background: var(--frame); }

  .panel { position: absolute; width: 188px; height: 420px; color: var(--ink-light); padding: 4px 3px 4px 4px; overflow: hidden; }
  .panel--cover { left: 40px; top: 40px; background: var(--black); padding: 0; }
  .panel--about { left: 248px; top: 40px; background: var(--yellow); padding: 80px 2px 0 4px; }
  .panel--sectors { left: 457px; top: 40px; background: var(--red); }
  .panel--warehouse { left: 559px; top: 443px; background: var(--green); }
  .panel--branding { left: 768px; top: 443px; background: var(--blue); }
  .panel--contact { left: 977px; top: 443px; background: var(--pink); padding: 250px 0 0 8px; }

  .heading {
    font-family: "Archivo Black", "Arial Black", sans-serif;
    color: var(--heading-ghost);
    letter-spacing: -0.12em;
    line-height: 1;
    text-transform: uppercase;
    white-space: nowrap;
    margin-bottom: 1px;
  }
  .heading--about { font-size: 35px; }
  .heading--wide { font-size: 33px; }
  .heading--word { font-size: 29px; }
  .heading--pair { font-size: 21px; }
  .heading--long { font-size: 15.5px; }
  .heading--contact { font-size: 28px; }

  .copy { font-size: 7px; line-height: 9.1px; letter-spacing: -0.1px; }
  .copy p + p { margin-top: 8px; }
  .about-copy { font-size: 8.5px; line-height: 10.5px; letter-spacing: -0.1px; }
  .about-copy p + p { margin-top: 10px; }
  .block + .block { margin-top: 9px; }

  .brand { position: absolute; left: 0; right: 0; top: 232px; text-align: center; }
  .brand__name { font-weight: 800; font-size: 58px; line-height: 1; color: var(--ink-light); }
  .brand__tagline { font-weight: 700; font-size: 7.4px; margin-top: 6px; letter-spacing: 0.2px; }
  .brand__web { font-weight: 800; font-size: 8.6px; letter-spacing: -0.1px; color: var(--link-blue); margin-top: 1px; white-space: nowrap; }
  .cover-photo { position: absolute; left: 0; bottom: 0; width: 188px; height: 106px; }

  .contact-copy { font-size: 9px; line-height: 11px; margin-top: 8px; }
  .contact-copy p + p { margin-top: 13px; }
</style>
</head>
<body>
<div class="canvas">

  <div class="sheet sheet--outside">
    <span class="fold" style="left:209px"></span>
    <span class="fold" style="left:419px"></span>
  </div>

  <div class="sheet sheet--inside">
    <span class="fold" style="left:209px"></span>
    <span class="fold" style="left:418px"></span>
  </div>

  <section class="panel panel--cover">
    <div class="brand">
      <div class="brand__name">B.W.C</div>
      <div class="brand__tagline">BRIGHTWALL COATINGS</div>
      <div class="brand__web">WWW.BRIGHTWALLCOATINGS.CO.NZ</div>
    </div>
    <svg class="cover-photo" viewBox="0 0 188 106" role="img" aria-label="Photo of a modern office interior with orange wall panels and white furniture">
      <defs>
        <linearGradient id="officeTone" x1="0" y1="0" x2="1" y2="1">
          <stop offset="0" stop-color="#e7e4df"/>
          <stop offset="0.55" stop-color="#c9a58a"/>
          <stop offset="1" stop-color="#8c8680"/>
        </linearGradient>
      </defs>
      <rect width="188" height="106" fill="url(#officeTone)"/>
    </svg>
  </section>

  <section class="panel panel--about">
    <h2 class="heading heading--about">About Us</h2>
    <div class="about-copy">
      <p>BWC are client focussed every step of the way, ensuring our communication is effective so that we understand your needs and can deliver a painting solution that meets them.</p>
      <p>BWC ensures that whatever we do you understand where we are coming from on a technical, practical or consultative level</p>
      <p>BWC past clients have really challenged us and helped us grow and develop our services. Check out what they have to say about their experience working with BWC by reading our testimonials.</p>
      <p>BWC are available throughout the Auckland region with a range of solutions and a variety of related services to offer. From interior design and colour consultancy to range of trade services we can set you up with one of our trusted affiliates to ensure you get the level of service you deserve.</p>
      <p>Whatever your needs, the vision for your Building BWC has the right combination of passion, knowledge and professionalism to get the job done.</p>
    </div>
  </section>

  <section class="panel panel--sectors">
    <div class="block">
      <h2 class="heading heading--pair">Office Buildings</h2>
      <p class="copy">B.W.C offers a wide range of services to All Building Owners and Occupants... Our team has expertise in all aspects of Interior and Exterior Coatings and Finishes , Reinstatement and demands that may be places on Modern Building.</p>
    </div>
    <div class="block">
      <h2 class="heading heading--long">Industrial Buildings</h2>
      <p class="copy">Commercial, Industrial, Factory, Warehouse, Production Facilities for all your Interior and Exterior Surfaces. Exterior Surfaces from Iron Roof, Colour Steel, Concrete Blocks, Tilt Slab Concrete Wall, Fiber Cement, Timber, Roller Doors, Windows,[ Steel, Timber, Aluminum] .Soffits, Canopies, Structural Steel, Interior Surfaces. Ceilings. [Suspended, Gibboard, Plaster.] Walls [Gibboard, Concrete, Timber, Wall coverings] Doors, Doorframes. Windows, [Steel, Timber, Aluminum] .Soffits, Canopies, Structural Steel, All Areas and Surfaces. Colour Coding Pipe Work, Coating of Concrete Floors, Machinery, Ducting, Production Lines, Mezzine Flooring, Commercial Ovens. To Support Offices, Production Areas, Passage Ways Corridors, Lunchroom, Workshops, Laboratories, Cafeterias, Toilets etc,etc.</p>
    </div>
    <div class="block">
      <h2 class="heading heading--pair">Retail Buildings</h2>
      <p class="copy">Retail, Showrooms, Restaurant, Bars, Shopping Malls &amp; Supermarkets for all your Interior and Exterior Surfaces. Exterior Surfaces from Iron Roof, Colour Steel Concrete Blocks, Tilt Slab Concrete Wall, Fiber Cement, Timber Weather Boards, Windows, [ Steel, Timber, Aluminum] .Soffits, Canopies, Structural Steel, Interior Surfaces. Ceilings. [Suspended, Gibboard, Plaster.] Walls [Gibboard, Concrete, Timber, Wall coverings] Doors, Doorframes. Windows, [Steel, Timber, Aluminum] .Soffits, Canopies, Structural Steel, All Areas and Surfaces. To Showroom, Retail Areas Passage Ways, Corridors, Lunchroom, Cafeterias, Toilets etc</p>
    </div>
  </section>

  <section class="panel panel--warehouse">
    <div class="block">
      <h2 class="heading heading--word">Warehouse</h2>
      <p class="copy">Commercial, Industrial, Factory, Warehouse, Production Facilities for all your Interior and Exterior Surfaces. Exterior Surfaces from Iron Roof, Colour Steel, Concrete Blocks, Tilt Slab Concrete Wall, Fiber Cement, Timber, Roller Doors, Windows, [ Steel, Timber, Aluminum] .Soffits, Canopies, Structural Steel, Interior Surfaces. Ceilings. [Suspended, Gibboard, Plaster.] Walls [Gibboard, Concrete, Timber, Wall coverings] Doors, Doorframes. Windows, [Steel, Timber, Aluminum] .Soffits, Canopies, Structural Steel, All Areas and Surfaces. Colour Coding Pipe Work, Coating of Concrete Floors, Machinery, Ducting, Production Lines, Mezzine Flooring, Commercial Ovens. To Support Offices, Production Areas, Passage Ways Corridors, Lunchroom, Workshops, Laboratories, Cafeterias, Toilets etc.</p>
    </div>
    <div class="block">
      <h2 class="heading heading--long">Commercial Buildings</h2>
      <p class="copy">Commercial, Industrial, Factory, Warehouse, Production Facilities for all your Interior and Exterior Surfaces. Exterior Surfaces from Iron Roof, Colour Steel, Concrete Blocks, Tilt Slab Concrete Wall, Fiber Cement, Timber, Roller Doors, Windows,[ Steel, Timber, Aluminum] .Soffits, Canopies, Structural Steel, Interior Surfaces. Ceilings. [Suspended, Gibboard, Plaster.] Walls [Gibboard, Concrete, Timber, Wall coverings] Doors, Doorframes. Windows, [Steel, Timber, Aluminum] .Soffits, Canopies, Structural Steel, All Areas and Surfaces. Colour Coding Pipe Work, Coating of Concrete Floors, Machinery, Ducting, Production Lines, Mezzine Flooring, Commercial Ovens. To Support Offices, Production Areas, Passage Ways Corridors, Lunchroom, Workshops, Laboratories, Cafeterias, Toilets etc,etc.</p>
    </div>
  </section>

  <section class="panel panel--branding">
    <div class="block">
      <h2 class="heading heading--wide">Branding</h2>
      <div class="copy">
        <p>Retail, Showrooms, Restaurant, Bars, Shopping Malls &amp; Supermarkets for all your Interior and Exterior Surfaces.<br>When a large company changes its name or other elements of its identity, the process needs to be implemented quickly to avoid confusion among customers, suppliers and the general public.</p>
        <p>One of the most important tasks in a re-branding programme - and perhaps the most logistically challenging - is the repainting of premises; this often involves completely changing the colour of possibly dozens of buildings around the country.</p>
        <p>BWC has a background of outstanding performance in this regard. To accomplish such a project successfully involves:</p>
        <p>Ensuring sufficient staff, materials and, possibly, subcontractors are available at multiple sites within a given timeframe<br>Ensuring all staff, equipment and vehicles meet a high standard of presentation.<br>B.W.C is able to meet these requirements and in doing so has transformed the appearance of many high-rises, warehouses, factories, apartment buildings, hospitals, rest homes, motels, office blocks and supermarkets.</p>
      </div>
    </div>
    <div class="block">
      <h2 class="heading heading--long">Historical Buildings</h2>
      <p class="copy">Churches, Town Halls, Goverment Buildings, Art Galleries, Public Buildings for all your Interior and Exterior Surfaces. Exterior Surfaces from Iron Roofs, Weather Boards, Windows,[ Steel, Timber, Aluminum] .Soffits, Interior Surfaces. Ceilings. [Suspended, Gibboard, Plaster.] Walls [Gibboard, Concrete, Timber, Wall coverings] Doors, Doorframes. Windows, [Steel, Timber, ] All Areas and Surfaces. BWC Has been involved in many Historcial Restoration of Buildings</p>
    </div>
  </section>

  <section class="panel panel--contact">
    <h2 class="heading heading--contact">Contact Us</h2>
    <div class="contact-copy">
      <p>Ph 021 555 0148<br>for Prompt and Personal Attention</p>
      <p>www.brightwallcoatings.co.nz</p>
    </div>
  </section>

</div>
</body>
</html>
```